Brightwave Reach - Business Card

We need a business card for a Social Media Marketing company that specializes in online marketing for small businesses in Canada using common Social Media platforms such as Pictora, Kinloop, Blinkit & Chirpo.

I have uploaded a copy of our logo which I would like utilized in the business card. We would like the business card to be modern yet classy design.

Our website is www.brightwavereach.ca

Industry/Entity Type

Marketing

Contact Information for Business Card

Email: info@brightwavereach.ca
Website: www.brightwavereach.ca
Telephone: 604-392-5108

Colors

Designer to choose colors to be used in the design.

Requirements
Must have
• Social Media icons on reverse
• Please add some designs with color.

```html
<!DOCTYPE html>
<html lang="en">
<head>
<meta charset="utf-8">
<title>Brightwave Reach – Business Card</title>
<link rel="stylesheet" href="https://fonts.googleapis.com/css2?family=Roboto:wght@400;500;900&display=swap">
<style>
  :root {
    --page-bg: #e9e7e4;
    --card-light: #ffffff;
    --card-dark: #3d4245;
    --ink: #3a3d40;
    --ink-soft: #55585b;
    --rule: #8a8c8e;
    --on-dark: #f4f4f4;
  }
  * { margin: 0; padding: 0; box-sizing: border-box; }
  html, body {
    width: 1200px; height: 1200px; overflow: hidden;
    background: var(--page-bg);
    font-family: "Roboto", Arial, sans-serif;
  }
  .canvas { position: relative; width: 1200px; height: 1200px; }
  .card {
    position: absolute; left: 210px; width: 780px; height: 444px;
    box-shadow: 0 4px 14px rgba(0,0,0,0.18);
  }
  .card-front { top: 140px; background: var(--card-light); color: var(--ink); }
  .card-back { top: 620px; background: var(--card-dark); color: var(--on-dark); }

  .wordmark {
    position: absolute; text-align: center;
    font-weight: 900; text-transform: uppercase; line-height: 0.98;
    letter-spacing: 0.5px;
  }
  .card-front .wordmark { left: 70px; width: 300px; top: 170px; font-size: 38px; color: var(--ink); }
  .card-back .wordmark { left: 240px; width: 300px; top: 172px; font-size: 38px; color: var(--on-dark); }

  .divider {
    position: absolute; left: 392px; top: 128px; width: 1.5px; height: 182px;
    background: var(--rule);
  }
  .contact { position: absolute; left: 428px; top: 140px; }
  .contact-name { font-size: 27px; font-weight: 500; color: var(--ink); line-height: 1.2; }
  .contact-role { font-size: 19px; color: var(--ink-soft); margin-top: 2px; }
  .contact-list { list-style: none; margin-top: 26px; }
  .contact-list li {
    display: flex; align-items: center; gap: 8px;
    font-size: 19px; color: var(--ink-soft); height: 28px;
  }
  .contact-list svg { width: 17px; height: 17px; flex: none; }

  .social-row {
    position: absolute; left: 0; right: 0; top: 386px;
    display: flex; justify-content: center; gap: 22px;
    font-size: 15px; font-weight: 500; color: var(--on-dark); letter-spacing: 0.3px;
  }
</style>
</head>
<body>
<div class="canvas">

  <section class="card card-front" aria-label="Card front">
    <div class="wordmark">Brightwave<br>Reach</div>
    <div class="divider"></div>
    <div class="contact">
      <div class="contact-name">Marcus Hale</div>
      <div class="contact-role">President &amp; CEO</div>
      <ul class="contact-list">
        <li>
          <svg viewBox="0 0 24 24" fill="none" stroke="currentColor" stroke-width="1.8" stroke-linejoin="round"><path d="M5 3h4l2 5-2.5 1.5a11 11 0 0 0 6 6L16 13l5 2v4a2 2 0 0 1-2 2A16 16 0 0 1 3 5a2 2 0 0 1 2-2z"/></svg>
          604-392-5108
        </li>
        <li>
          <svg viewBox="0 0 24 24" fill="none" stroke="currentColor" stroke-width="1.8"><rect x="3" y="5" width="18" height="14"/><path d="M3 5l9 8 9-8"/></svg>
          info@brightwavereach.ca
        </li>
        <li>
          <svg viewBox="0 0 24 24" fill="none" stroke="currentColor" stroke-width="1.8"><circle cx="12" cy="12" r="9"/><path d="M3 12h18M12 3c3 3 3 15 0 18M12 3c-3 3-3 15 0 18"/></svg>
          www.brightwavereach.ca
        </li>
      </ul>
    </div>
  </section>

  <section class="card card-back" aria-label="Card back">
    <div class="wordmark">Brightwave<br>Reach</div>
    <div class="social-row">
      <span>Kinloop</span>
      <span>Linkwell</span>
      <span>Chirpo</span>
      <span>Callbeam</span>
    </div>
  </section>

</div>
</body>
</html>
```